Business Card Design

It's an investment advisory service for individuals with all there investment needs. Also financial consulting to businesses and governmental agencies on retirement plans etc. It's personalized not commoditized help. Should show strength, knowledge and money orientation.

Industry/Entity Type

Investment

Contact Information for Business Card

B. Vel R. Financial Consulting and Wealth Management, Mirek Dale Hopstein, 5172 Paseo Las Colinas Verde, San Diego, CA 92084-6617, Registered Investment Advisor

Requirements
Nice to have
• Something money oriented

```html
<!DOCTYPE html>
<html lang="en">
<head>
<meta charset="utf-8">
<title>B. Vel R. Financial Consulting &amp; Wealth Management — Business Card</title>
<link rel="stylesheet" href="https://fonts.googleapis.com/css2?family=Open+Sans:wght@400;600;700&display=swap">
<style>
  :root {
    --band-black: #141414;
    --card-black: #151515;
    --paper-white: #f4f4f4;
    --stage: #d9d6d1;
    --rule-light: #e4e4e4;
    --money-green: #2f7a47;
    --deep-green: #1f5530;
    --text-light: #f2f2f2;
    --text-dark: #1b1b1b;
  }
  * { box-sizing: border-box; margin: 0; padding: 0; }
  html, body { width: 1200px; height: 1000px; overflow: hidden; }
  body {
    font-family: "Open Sans", Arial, sans-serif;
    background: var(--stage);
    position: relative;
  }

  /* Brand header band */
  .brand-band {
    position: absolute; left: 0; top: 0;
    width: 1200px; height: 245px;
    background: var(--band-black);
    display: flex; align-items: center; justify-content: center;
  }
  .brand-rule {
    position: absolute; left: 0; top: 245px;
    width: 1200px; height: 8px;
    background: var(--rule-light);
  }

  /* Name lockup (name only, one colour, one weight) */
  .lockup { display: flex; align-items: center; gap: 22px; }
  .lockup-dot {
    width: 34px; height: 34px; border-radius: 50%;
    background: var(--money-green); flex: none;
  }
  .lockup-name {
    font-weight: 600;
    line-height: 1.18;
    color: var(--text-light);
    white-space: nowrap;
  }
  .brand-band .lockup-name { font-size: 32px; }

  /* Cards */
  .card {
    position: absolute;
    width: 500px; height: 286px;
    top: 520px;
    box-shadow: 0 14px 30px rgba(0,0,0,0.22);
    overflow: hidden;
  }
  .card-front {
    left: 70px;
    background: var(--card-black);
    display: flex; align-items: center; justify-content: center;
  }
  .card-front .lockup-name { font-size: 21px; }
  .card-front .lockup-dot { width: 22px; height: 22px; }
  .card-front .lockup { gap: 14px; }

  .card-back {
    left: 630px;
    background: var(--paper-white);
    color: var(--text-dark);
  }
  .card-back .lockup {
    position: absolute; left: 20px; bottom: 30px; gap: 9px;
  }
  .card-back .lockup-dot { width: 16px; height: 16px; }
  .card-back .lockup-name { font-size: 12.5px; color: var(--deep-green); }

  .divider-vertical {
    position: absolute; left: 254px; top: 104px; bottom: 0;
    width: 1px; background: var(--text-dark);
  }
  .divider-horizontal {
    position: absolute; left: 254px; right: 0; top: 104px;
    height: 1px; background: var(--text-dark);
  }

  .advisor {
    position: absolute; right: 26px; top: 48px; text-align: right;
  }
  .advisor-name { font-size: 21px; font-weight: 700; letter-spacing: 0.2px; }
  .advisor-title { font-size: 12px; color: var(--money-green); margin-top: 2px; }

  .contact-list {
    position: absolute; right: 26px; top: 126px;
    list-style: none; text-align: right;
    font-size: 12.5px; line-height: 1.55;
  }
  .contact-list li { display: flex; justify-content: flex-end; align-items: center; gap: 7px; }
  .contact-list .address-line { padding-right: 19px; }
  .contact-icon {
    width: 12px; height: 12px; flex: none;
    border-radius: 50%; background: var(--deep-green);
    display: inline-flex; align-items: center; justify-content: center;
  }
  .contact-icon svg { width: 8px; height: 8px; fill: #fff; }
  .contact-group { margin-top: 10px; }
</style>
</head>
<body>

  <header class="brand-band">
    <div class="lockup">
      <span class="lockup-dot"></span>
      <div class="lockup-name">B. Vel R. Financial Consulting<br>&amp; Wealth Management</div>
    </div>
  </header>
  <div class="brand-rule"></div>

  <section class="card card-front" aria-label="Card front">
    <div class="lockup">
      <span class="lockup-dot"></span>
      <div class="lockup-name">B. Vel R. Financial Consulting<br>&amp; Wealth Management</div>
    </div>
  </section>

  <section class="card card-back" aria-label="Card back">
    <div class="advisor">
      <div class="advisor-name">Mirek Dale Hopstein</div>
      <div class="advisor-title">Registered Investment Advisor</div>
    </div>
    <div class="divider-horizontal"></div>
    <div class="divider-vertical"></div>

    <ul class="contact-list">
      <li>01234 908172
        <span class="contact-icon"><svg viewBox="0 0 10 10"><path d="M2 1h2l1 2.5-1.2.8a5 5 0 0 0 1.9 1.9l.8-1.2L9 6v2c0 .6-.4 1-1 1A7 7 0 0 1 1 2c0-.6.4-1 1-1z"/></svg></span>
      </li>
      <li>mail@bvelrwealth.com
        <span class="contact-icon"><svg viewBox="0 0 10 10"><path d="M1 2.5h8v5H1z M1 2.5l4 3 4-3" fill="none" stroke="#fff" stroke-width="1"/></svg></span>
      </li>
      <li>www.bvelrwealth.com
        <span class="contact-icon"><svg viewBox="0 0 10 10"><circle cx="5" cy="5" r="3.6" fill="none" stroke="#fff" stroke-width="0.9"/><path d="M1.4 5h7.2M5 1.4c-1.6 2-1.6 5.2 0 7.2M5 1.4c1.6 2 1.6 5.2 0 7.2" fill="none" stroke="#fff" stroke-width="0.8"/></svg></span>
      </li>
      <li class="contact-group">5172 Paseo Las Colinas Verde
        <span class="contact-icon"><svg viewBox="0 0 10 10"><path d="M5 9S2 5.6 2 3.8a3 3 0 0 1 6 0C8 5.6 5 9 5 9z"/></svg></span>
      </li>
      <li class="address-line">San Diego, CA 92084-6617</li>
    </ul>

    <div class="lockup">
      <span class="lockup-dot"></span>
      <div class="lockup-name">B. Vel R. Financial Consulting<br>&amp; Wealth Management</div>
    </div>
  </section>

</body>
</html>
```